Clothing for elderly and disabled persons business card

I have seen a design on the Pelto website with a partial hand holding a heart I would like that to be incorporated above the i in Marigold
The colours should be either soft green and pinks.
The final design should communicate care, love, easy fit comfort clothing for the frail and disabled.

Marigold
Assisted CareClothing

Target Market(s)

Nursing Homes, Elderly in care or just anyone with limited mobility

Industry/Entity Type

Clothing

Contact Information for Business Card

Marigold Assisted Care Clothing
Karen Lowther Owner Sales Consultant
Phone 0461 752 038 Fax 08 9627 4083
Email: marigoldassistedclothing@fernpost.net
Website: ?????? to be created

Requirements
Nice to have
• A hand holding a heart this must form part of the i in Marigold, instead of the dot above the i I want the hand holding the heart.

```html
<!DOCTYPE html>
<html lang="en">
<head>
<meta charset="utf-8">
<title>Marigold Assisted Care Clothing – Business Card</title>
<link rel="stylesheet" href="https://fonts.googleapis.com/css2?family=Open+Sans:wght@400;600&display=swap">
<style>
  :root {
    --backdrop: #e9e9e9;
    --card: #ffffff;
    --blush: #f1bcc0;
    --blush-deep: #eba9ae;
    --ink: #3a3a3a;
    --ink-soft: #555555;
    --shadow: rgba(0, 0, 0, 0.18);
  }
  * { box-sizing: border-box; margin: 0; padding: 0; }
  html, body {
    width: 1200px;
    height: 900px;
    overflow: hidden;
    background: var(--backdrop);
    font-family: "Open Sans", Arial, sans-serif;
  }
  .canvas {
    position: relative;
    width: 1200px;
    height: 900px;
  }
  .business-card {
    position: absolute;
    left: 120px;
    top: 176px;
    width: 960px;
    height: 548px;
    background: var(--card);
    box-shadow: 0 10px 30px var(--shadow);
    overflow: hidden;
  }
  .brand {
    position: absolute;
    left: 84px;
    top: 92px;
    display: flex;
    align-items: center;
    gap: 18px;
  }
  .brand-mark {
    width: 46px;
    height: 46px;
    border-radius: 50%;
    background: var(--blush);
    flex: none;
  }
  .brand-name {
    color: var(--blush-deep);
    font-weight: 600;
    font-size: 40px;
    line-height: 1.15;
    letter-spacing: 0.5px;
  }
  .contact {
    position: absolute;
    left: 478px;
    top: 218px;
    color: var(--ink);
  }
  .contact-name {
    font-size: 30px;
    font-weight: 400;
    letter-spacing: 0.2px;
  }
  .contact-name .divider {
    margin: 0 10px;
    color: var(--ink-soft);
  }
  .contact-role {
    font-size: 22px;
    letter-spacing: 0.5px;
  }
  .contact-email {
    margin-top: 6px;
    font-size: 19px;
    color: var(--ink-soft);
  }
  .contact-lines {
    list-style: none;
    margin-top: 52px;
    margin-left: 36px;
  }
  .contact-lines li {
    display: flex;
    align-items: center;
    gap: 14px;
    font-size: 21px;
    line-height: 1.55;
  }
  .contact-lines svg {
    width: 22px;
    height: 22px;
    flex: none;
  }
  .card-band {
    position: absolute;
    left: 0;
    right: 0;
    bottom: 0;
    height: 58px;
    background: var(--blush);
  }
</style>
</head>
<body>
<main class="canvas">
  <section class="business-card" aria-label="Business card">
    <div class="brand">
      <span class="brand-mark" aria-hidden="true"></span>
      <div class="brand-name">Marigold Assisted<br>Care Clothing</div>
    </div>

    <div class="contact">
      <p class="contact-name">Karen Lowther<span class="divider">|</span><span class="contact-role">OWNER</span></p>
      <p class="contact-email">marigoldassistedclothing@fernpost.net</p>
      <ul class="contact-lines">
        <li>
          <svg viewBox="0 0 24 24" aria-hidden="true">
            <rect x="3" y="3" width="18" height="18" rx="2" fill="none" stroke="#3a3a3a" stroke-width="2"/>
            <rect x="6" y="6" width="4" height="12" fill="#3a3a3a"/>
            <rect x="12" y="7" width="2.5" height="2.5" fill="#3a3a3a"/>
            <rect x="16" y="7" width="2.5" height="2.5" fill="#3a3a3a"/>
            <rect x="12" y="11" width="2.5" height="2.5" fill="#3a3a3a"/>
            <rect x="16" y="11" width="2.5" height="2.5" fill="#3a3a3a"/>
            <rect x="12" y="15" width="2.5" height="2.5" fill="#3a3a3a"/>
            <rect x="16" y="15" width="2.5" height="2.5" fill="#3a3a3a"/>
          </svg>
          <span>0461 752 038 (sales consultant)</span>
        </li>
        <li>
          <svg viewBox="0 0 24 24" aria-hidden="true">
            <rect x="7" y="2" width="10" height="8" fill="none" stroke="#3a3a3a" stroke-width="2"/>
            <rect x="3" y="10" width="18" height="11" rx="1.5" fill="#3a3a3a"/>
            <rect x="7" y="14" width="10" height="2" fill="#ffffff"/>
          </svg>
          <span>08 9627 4083 (fax)</span>
        </li>
      </ul>
    </div>

    <div class="card-band" aria-hidden="true"></div>
  </section>
</main>
</body>
</html>
```